Bath Salt - Sachet Packet (5 Scents) Packaging Design

We sell products to professional salons in the USA. This product is used as the first step when treating clients to a pedicure spa. This product is called SALT SOAK (or Bath Salts). The salt is added to the water to cleanse the skin, create a pleasant fragrance, and change the color of the water.

This product has 5 different variations, based on the scent of the salt soak. The available scents are:
LAVENDER, MANDARIN, CUCUMBER-MELON, JASMINE, MINT.

We would like to see package designs for all 5 scents. The theme should be consistent across the different variations of scents. The design should focus on bright, attractive, floral colors/themes. The design should fully express the color and imagery that are associated with each scent. (Lavender scent should include purple colors, lavender flower, etc.). See example images for reference of popular designs/brands.

Ideal designs will incorporate a luxurious and premium aesthetic that combines elegant imagery, colors, and premium finishes. See example images for reference of popular designs/brands.

Each packet is individually sealed. See dimension artwork file for reference of the sachet packet size and layout.

See the attached document guidelines for more information about product name, key text, and brand logo.

Target Market(s)

Beauty & Nail Salons

Industry/Entity Type

Beauty

Font styles to use
Sans Serif
Script

Requirements
Must have
• Bright imagery and colors that relate to the target fragrance
Nice to have
• Premium and luxurious finishes (shiny accent, etc.)

```html
<!DOCTYPE html>
<html lang="en">
<head>
<meta charset="utf-8">
<title>Velune Sea Salt Soak – Lavender</title>
<link rel="stylesheet" href="https://fonts.googleapis.com/css2?family=Bebas+Neue&family=Montserrat:wght@500;600;700&display=swap">
<style>
  :root {
    --stage: #3a2158;
    --band: #7b6198;
    --band-edge: #4b2a82;
    --body-light: #ddd3e4;
    --body-mid: #c9bdd3;
    --ink: #1c1036;
    --accent: #4a2a7e;
    --pale: #ece6f2;
    --foot: #8a72a8;
    --art-purple: #8c70b0;
    --art-green: #a9c24a;
  }
  * { box-sizing: border-box; margin: 0; padding: 0; }
  html, body { width: 1200px; height: 960px; overflow: hidden; }
  body { background: var(--stage); position: relative; font-family: "Montserrat", sans-serif; }

  .sachet {
    position: absolute;
    top: 160px;
    width: 437px;
    height: 646px;
    border-radius: 26px;
    overflow: hidden;
    background: linear-gradient(100deg, var(--body-mid) 0%, var(--body-light) 55%, var(--body-mid) 100%);
  }
  .sachet--left { left: 141px; }
  .sachet--right { left: 622px; }

  .sachet__top { position: absolute; inset: 0; width: 437px; height: 646px; }

  .sachet__kicker {
    position: absolute; top: 36px; left: 0; width: 100%;
    text-align: center; font-weight: 600; font-size: 18px;
    letter-spacing: 4.5px; color: var(--pale);
  }
  .sachet__brand {
    position: absolute; top: 104px; left: 0; width: 100%;
    display: flex; justify-content: center; align-items: center; gap: 12px;
    font-weight: 600; font-size: 50px; letter-spacing: 2px; color: var(--pale);
  }
  .sachet__brand-dot { width: 12px; height: 12px; border-radius: 50%; background: var(--pale); }

  .sachet__title {
    position: absolute; top: 246px; left: 0; width: 100%;
    text-align: center; font-family: "Bebas Neue", sans-serif;
    font-size: 72px; line-height: 1; color: var(--ink); letter-spacing: 0.5px;
  }
  .sachet__scent {
    position: absolute; top: 316px; left: 0; width: 100%;
    display: flex; justify-content: center; align-items: center; gap: 16px;
    font-weight: 700; font-size: 40px; letter-spacing: 1.5px; color: var(--accent);
  }
  .sachet__dash { width: 30px; height: 2px; background: var(--accent); border-radius: 2px; }

  .sachet__art {
    position: absolute; top: 386px; left: 138px; width: 161px; height: 178px;
    border-radius: 50% 50% 40% 40%;
    background: radial-gradient(circle at 50% 30%, var(--art-purple) 0%, rgba(140,112,176,0.5) 40%, rgba(169,194,74,0.55) 75%, rgba(169,194,74,0) 100%);
  }

  .sachet__claims {
    position: absolute; top: 587px; left: 0; width: 100%;
    text-align: center; font-weight: 600; font-size: 12px;
    letter-spacing: 0.3px; color: var(--accent); word-spacing: 1px;
  }
  .sachet__foot {
    position: absolute; left: 0; bottom: 0; width: 100%; height: 32px;
    background: var(--foot);
    display: flex; justify-content: center; align-items: center;
    font-weight: 500; font-size: 13px; letter-spacing: 0.5px; color: var(--pale);
  }
</style>
</head>
<body>

  <section class="sachet sachet--left">
    <svg class="sachet__top" viewBox="0 0 437 646" aria-hidden="true">
      <path d="M0 0 H437 V142 C395 140 378 165 370 188 C350 180 332 188 323 205 C280 182 230 190 199 222 C160 180 100 175 58 188 C50 160 30 146 0 144 Z" fill="var(--band)"/>
      <path d="M0 144 C30 146 50 160 58 188 C100 175 160 180 199 222 C230 190 280 182 323 205 C332 188 350 180 370 188 C378 165 395 140 437 142" fill="none" stroke="var(--band-edge)" stroke-width="4"/>
    </svg>
    <p class="sachet__kicker">DELUXE PEDICURE</p>
    <div class="sachet__brand"><span class="sachet__brand-dot"></span>VELUNE</div>
    <h1 class="sachet__title">SEA SALT SOAK</h1>
    <p class="sachet__scent"><span class="sachet__dash"></span>LAVENDER<span class="sachet__dash"></span></p>
    <div class="sachet__art" role="img" aria-label="Line illustration of a lavender sprig with purple blossoms and green leaves"></div>
    <p class="sachet__claims">VEGAN &nbsp;|&nbsp; SINGLE-USE &nbsp;|&nbsp; SEALED FRESH &nbsp;|&nbsp; PARABEN FREE</p>
    <p class="sachet__foot">NET WT. 12 OZ</p>
  </section>

  <section class="sachet sachet--right">
    <svg class="sachet__top" viewBox="0 0 437 646" aria-hidden="true">
      <path d="M0 0 H437 V142 C395 140 378 165 370 188 C350 180 332 188 323 205 C280 182 230 190 199 222 C160 180 100 175 58 188 C50 160 30 146 0 144 Z" fill="var(--band)"/>
      <path d="M0 144 C30 146 50 160 58 188 C100 175 160 180 199 222 C230 190 280 182 323 205 C332 188 350 180 370 188 C378 165 395 140 437 142" fill="none" stroke="var(--band-edge)" stroke-width="4"/>
    </svg>
    <p class="sachet__kicker">DELUXE PEDICURE</p>
    <div class="sachet__brand"><span class="sachet__brand-dot"></span>VELUNE</div>
    <h2 class="sachet__title">SEA SALT SOAK</h2>
    <p class="sachet__scent"><span class="sachet__dash"></span>LAVENDER<span class="sachet__dash"></span></p>
    <div class="sachet__art" role="img" aria-label="Line illustration of a lavender sprig with purple blossoms and green leaves"></div>
    <p class="sachet__claims">VEGAN &nbsp;|&nbsp; SINGLE-USE &nbsp;|&nbsp; SEALED FRESH &nbsp;|&nbsp; PARABEN FREE</p>
    <p class="sachet__foot">NET WT. 12 OZ</p>
  </section>

</body>
</html>
```